I'm an electrician and the name of my company is called Brisk 'N' Bright Electrical. I require a professional business card that speaks to my clients, I also need it to be innovative and modern. We do maintenance & service work for domestic and commercial premises.

Industry/Entity Type

Electrical

Contact Information for Business Card

Must have the name of my company Brisk 'N' Bright Electrical, my name Darren Kolovos and my contact details 0427 381 592 and company email address Brisknbrightelectrical@mailvane.com and/or website Brisknbrightelectrical.com.au

Logo Text

Brisk 'N' Bright Electrical (If possible)

Colors
33a6d7
0592cd
3176b5

```html
<!DOCTYPE html>
<html lang="en">
<head>
<meta charset="utf-8">
<title>Brisk 'N' Bright Electrical – Business Card</title>
<link rel="stylesheet" href="https://fonts.googleapis.com/css2?family=Montserrat:wght@400;500;800&display=swap">
<style>
  :root {
    --sky: #33a6d7;
    --azure: #0592cd;
    --steel: #3176b5;
    --signal-red: #e8202a;
    --ink: #111418;
    --paper: #ffffff;
    --backdrop: #e9ecef;
    --rule: #c9ced3;
  }
  * { box-sizing: border-box; margin: 0; padding: 0; }
  html, body { width: 1200px; height: 1054px; overflow: hidden; }
  body {
    background: var(--backdrop);
    font-family: "Montserrat", sans-serif;
    color: var(--ink);
    position: relative;
  }
  .card {
    position: absolute;
    left: 185px;
    width: 830px;
    height: 461px;
    background: var(--paper);
    border-radius: 18px;
    overflow: hidden;
    box-shadow: 0 6px 22px rgba(0,0,0,.18);
  }
  .card--back { top: 44px; }
  .card--front { top: 549px; }
  .card__art { position: absolute; inset: 0; width: 100%; height: 100%; }

  .brand-name {
    position: absolute;
    font-weight: 800;
    color: var(--ink);
    text-transform: uppercase;
    line-height: 1.05;
    letter-spacing: .5px;
    text-align: center;
  }
  .card--back .brand-name { left: 40px; top: 175px; width: 380px; font-size: 38px; }
  .card--front .brand-name { left: 30px; top: 165px; width: 340px; font-size: 36px; }

  .details { position: absolute; white-space: nowrap; }
  .card--back .details { left: 505px; top: 92px; }
  .card--front .details { left: 440px; top: 100px; }

  .company-line { font-size: 16px; font-weight: 500; letter-spacing: .4px; text-transform: uppercase; }
  .company-line__lead { color: var(--steel); }
  .company-line__trade { color: var(--signal-red); }

  .person-name { font-weight: 800; text-transform: uppercase; letter-spacing: .3px; }
  .card--back .person-name { font-size: 19px; margin-top: 4px; }
  .card--front .person-name { font-size: 30px; }
  .person-name__first { color: var(--signal-red); }

  .contact-list { list-style: none; margin-top: 14px; }
  .contact-list li {
    display: flex; align-items: center; gap: 12px;
    font-size: 13px; font-weight: 400; height: 32px;
  }
  .card--front .contact-list li { font-size: 14px; }
  .contact-list svg { width: 20px; height: 20px; flex: none; }

  .divider {
    position: absolute; left: 410px; top: 100px;
    width: 1px; height: 200px; background: var(--rule);
  }
</style>
</head>
<body>

<section class="card card--back" aria-label="Business card, logo side">
  <svg class="card__art" viewBox="0 0 830 461" aria-hidden="true">
    <path d="M0 0 H272 C462 40 512 230 462 461 H0 Z" fill="var(--signal-red)"/>
    <path d="M0 0 H260 C450 40 500 230 450 461 H0 Z" fill="var(--sky)"/>
  </svg>
  <p class="brand-name">Brisk 'N' Bright Electrical</p>

  <div class="details">
    <p class="company-line"><span class="company-line__lead">Brisk 'N' Bright</span> <span class="company-line__trade">Electrical</span></p>
    <p class="person-name">Darren Kolovos</p>
    <ul class="contact-list">
      <li><svg viewBox="0 0 20 20" fill="none" stroke="var(--steel)" stroke-width="1.4"><rect x="1" y="1" width="18" height="18" rx="4"/><path d="M6 5l2 0 1 3-1.5 1a7 7 0 0 0 3.5 3.5l1-1.5 3 1v2a1.5 1.5 0 0 1-1.5 1.5A10 10 0 0 1 4.5 6.5 1.5 1.5 0 0 1 6 5z"/></svg>0427 381 592</li>
      <li><svg viewBox="0 0 20 20" fill="none" stroke="var(--steel)" stroke-width="1.4"><rect x="1.5" y="4" width="17" height="12" rx="1"/><path d="M1.5 4l8.5 7 8.5-7"/></svg>Brisknbrightelectrical@mailvane.com</li>
      <li><svg viewBox="0 0 20 20" fill="none" stroke="var(--steel)" stroke-width="1.4"><circle cx="10" cy="10" r="8.5"/><ellipse cx="10" cy="10" rx="3.5" ry="8.5"/><path d="M1.5 10h17M3 5.5h14M3 14.5h14"/></svg>Brisknbrightelectrical.com.au</li>
    </ul>
  </div>
</section>

<section class="card card--front" aria-label="Business card, contact side">
  <svg class="card__art" viewBox="0 0 830 461" aria-hidden="true">
    <path d="M0 461 V432 C260 350 600 370 830 285 V461 Z" fill="var(--sky)"/>
    <path d="M20 461 C270 370 610 390 830 305" fill="none" stroke="var(--paper)" stroke-width="3"/>
    <path d="M0 461 V450 C260 390 610 400 830 320 V461 Z" fill="var(--azure)" opacity=".35"/>
  </svg>
  <p class="brand-name">Brisk 'N' Bright Electrical</p>
  <div class="divider"></div>

  <div class="details">
    <p class="person-name"><span class="person-name__first">Darren</span> Kolovos</p>
    <ul class="contact-list">
      <li><svg viewBox="0 0 20 20" fill="none" stroke="var(--ink)" stroke-width="1.4"><rect x="1" y="1" width="18" height="18" rx="4"/><path d="M6 5l2 0 1 3-1.5 1a7 7 0 0 0 3.5 3.5l1-1.5 3 1v2a1.5 1.5 0 0 1-1.5 1.5A10 10 0 0 1 4.5 6.5 1.5 1.5 0 0 1 6 5z"/></svg>0427 381 592</li>
      <li><svg viewBox="0 0 20 20" fill="none" stroke="var(--ink)" stroke-width="1.4"><rect x="1.5" y="4" width="17" height="12" rx="1"/><path d="M1.5 4l8.5 7 8.5-7"/></svg>Brisknbrightelectrical@mailvane.com</li>
      <li><svg viewBox="0 0 20 20" fill="none" stroke="var(--ink)" stroke-width="1.4"><circle cx="10" cy="10" r="8.5"/><ellipse cx="10" cy="10" rx="3.5" ry="8.5"/><path d="M1.5 10h17M3 5.5h14M3 14.5h14"/></svg>Brisknbrightelectrical.com.au</li>
    </ul>
  </div>
</section>

</body>
</html>
```